Summit Grading a Masonry LLC business card

My current business card is very plain. it has my logo and contact information. I woud like something that stands out from the rest. please take a look at my website to see about my company.

Compayt Name - Summit Grading And Masonry
Owner - Martin Galloway
Business Address
Business Website - www.summitgradingandmasonry.example
Email - Summitgradingandmasonry@mailbox.example
Phone - 555-214-3867
Fax - 555-630-2719

Target Market(s)

Everyone age tang is 18 - 85

Industry/Entity Type

Business

Contact Information for Business Card

Nice and professional all in one.

Font styles to use
Serif
Other font styles liked:
• Up to you

Requirements
Must have
• All contact info. The design is up to you.
Nice to have
• All the contact info the design is up to you
Should not have
• I don't have any

```html
<!DOCTYPE html>
<html lang="en">
<head>
<meta charset="utf-8">
<title>Summit Grading And Masonry – Business Card</title>
<link href="https://fonts.googleapis.com/css2?family=Roboto+Slab:wght@300&family=Alfa+Slab+One&family=Nunito:wght@400;600&display=swap" rel="stylesheet">
<style>
  :root {
    --bg: #1f2430;
    --card-white: #f4f4f4;
    --ink-black: #1e1e1e;
    --brand-green: #6ab544;
    --slate: #5d6870;
    --text-grey: #6c6c6c;
    --panel-grey: #dcdcdc;
    --block-neutral: #b9bdc1;
  }
  * { box-sizing: border-box; margin: 0; padding: 0; }
  html, body { width: 1200px; height: 900px; overflow: hidden; }
  body {
    background: var(--bg);
    display: flex;
    flex-direction: column;
    align-items: center;
    justify-content: center;
    gap: 36px;
    font-family: "Nunito", sans-serif;
  }
  .card {
    width: 700px;
    height: 400px;
    position: relative;
    overflow: hidden;
    box-shadow: 0 10px 30px rgba(0,0,0,.45);
  }

  /* Front */
  .card-front {
    background: linear-gradient(160deg, #ffffff 0%, var(--card-white) 60%, #e9e9e9 100%);
    text-align: center;
  }
  .top-accent {
    position: absolute;
    top: 0; left: 250px;
    width: 220px; height: 9px;
    background: var(--brand-green);
  }
  .owner-name {
    position: absolute;
    top: 56px; left: 0; right: 0;
    font-family: "Roboto Slab", serif;
    font-weight: 300;
    font-size: 58px;
    line-height: 1.2;
    color: var(--brand-green);
    letter-spacing: -0.5px;
  }
  .contact-list {
    position: absolute;
    top: 140px; left: 0; right: 0;
    list-style: none;
    font-size: 19px;
    line-height: 1.45;
    color: var(--text-grey);
  }
  .divider-dash {
    position: absolute;
    top: 245px; left: 328px;
    width: 44px; height: 5px;
    background: var(--brand-green);
  }
  .company-name {
    position: absolute;
    top: 278px; left: 0; right: 0;
    font-family: "Alfa Slab One", serif;
    font-size: 33px;
    letter-spacing: 1.5px;
    color: var(--slate);
    text-transform: uppercase;
  }
  .address-band {
    position: absolute;
    bottom: 0; left: 0; right: 0;
    height: 62px;
    background: var(--ink-black);
    color: var(--brand-green);
    font-size: 20px;
    display: flex;
    align-items: center;
    justify-content: center;
  }

  /* Back */
  .card-back {
    background: linear-gradient(180deg, #ececec 0%, var(--panel-grey) 100%);
    text-align: center;
  }
  .headline-band {
    position: absolute;
    top: 0; left: 0; right: 0;
    height: 118px;
    background: var(--ink-black);
    border-bottom: 7px solid var(--brand-green);
    padding-top: 20px;
  }
  .headline {
    font-family: "Alfa Slab One", serif;
    font-size: 30px;
    letter-spacing: 3px;
    color: #ffffff;
  }
  .tagline {
    font-size: 27px;
    font-weight: 600;
    color: var(--brand-green);
    margin-top: 2px;
  }
  .back-company {
    position: absolute;
    top: 148px; left: 0; right: 0;
    font-family: "Alfa Slab One", serif;
    font-size: 31px;
    letter-spacing: 1.5px;
    color: var(--slate);
  }
  .badge-row {
    position: absolute;
    top: 228px; left: 0; right: 0;
    display: flex;
    justify-content: space-around;
    align-items: center;
    padding: 0 90px;
  }
  .badge-block {
    width: 96px;
    height: 76px;
    background: var(--block-neutral);
    border-radius: 6px;
  }
  .footer-band {
    position: absolute;
    bottom: 0; left: 0; right: 0;
    height: 38px;
    background: var(--ink-black);
  }
</style>
</head>
<body>

  <section class="card card-front" aria-label="Business card front">
    <div class="top-accent"></div>
    <h1 class="owner-name">Martin Galloway</h1>
    <ul class="contact-list">
      <li>Summitgradingandmasonry@mailbox.example</li>
      <li>Phone - 555-214-3867</li>
      <li>Fax - 555-630-2719</li>
    </ul>
    <div class="divider-dash"></div>
    <p class="company-name">Summit Grading &amp; Masonry</p>
    <p class="address-band">2740 Harbor Lane, Millbrook, NY, United States</p>
  </section>

  <section class="card card-back" aria-label="Business card back">
    <div class="headline-band">
      <p class="headline">HAVE AN ASPHALT PROBLEM?</p>
      <p class="tagline">We Can Help!</p>
    </div>
    <p class="back-company">SUMMIT GRADING &amp; MASONRY</p>
    <div class="badge-row">
      <div class="badge-block" role="img" aria-label="Partner rating badge"></div>
      <div class="badge-block" role="img" aria-label="Screening certificate badge"></div>
      <div class="badge-block" role="img" aria-label="Service award badge"></div>
    </div>
    <div class="footer-band"></div>
  </section>

</body>
</html>
```